car site and logo design

I am looking for a clean website that is easy to navigate to view and post used cars for sale. The required tabs are [Buy - Sell - News - Care Tips - Finance - Insurance - FAQ]
motorlane.example has a great search tool on the landing page. New & Zip code are not required.
wexa autos has a nice simple results display, although I am open to other neat clean layouts.
Users can create an account or login using their pinloop accounts, and follow, like, comment on other users posted cars. sellers can be given ratings as well.
displaying car information should be neat and simple, showing the seller name which can be clicked on and takes the viewer to the seller page to view other cars for sale if any. included in the car information when viewing a specific car a bell curve showing the prices available for the same car being sold on the site, and the position of this particular car.
the care tips, finance and insurance pages will have rectangular boxes with sponsored ads by the related companies.
the logo should be a cartoon style mechanic character, with a slogan next to it [buying a ride?, selling a ride?, ride adive? Query Tobin ] - the site will be called querytobin.
Sell tab would include a quick post box where user inserts the vehicle VIN number and will open a page where user will just have to upload the remaining data such as mileage, color, etc.
this is basically what the site is about.

Target Market(s)

target market will be older generation looking to buy and sell a car, will require easy features, as well as younger crowd who are familiar with using extra features.

Industry/Entity Type

Finance

Requirements
Nice to have
• site should have a light sense of social media site where user has a profile photo, can view user's history and activity

```html
<!DOCTYPE html>
<html lang="en">
<head>
<meta charset="utf-8">
<title>Query Tobin – Used Cars</title>
<link href="https://fonts.googleapis.com/css2?family=PT+Sans:ital,wght@0,400;0,700;1,400&family=PT+Sans+Narrow:wght@400;700&display=swap" rel="stylesheet">
<style>
:root{
  --red:#c4161c;
  --red-dark:#9e0f13;
  --ink:#333;
  --muted:#666;
  --grey-band:#e4e4e4;
  --light:#f4f4f4;
  --footer:#1c232b;
  --white:#fff;
}
*{box-sizing:border-box;margin:0;padding:0}
html,body{width:773px;height:1200px;overflow:hidden}
body{position:relative;background:var(--white);font-family:"PT Sans",sans-serif;color:var(--ink)}
.abs{position:absolute}
/* header */
.mascot{left:86px;top:2px;width:64px;height:104px;background:linear-gradient(#d8383c,#4c6a8a);border-radius:30px 30px 8px 8px;z-index:3}
.brand{left:188px;top:14px;font-size:24px;color:var(--red);font-variant:small-caps;letter-spacing:.5px}
.tagline{left:188px;top:47px;font-size:10px;color:#555}
.phone{left:508px;top:0;width:158px;height:26px;background:#eee;border-radius:0 0 40px 40px;display:flex;align-items:center;justify-content:center;gap:6px;font-size:15px;color:#222}
.search{left:495px;top:42px;width:128px;height:19px;border:1px solid #ddd;font-size:8px;color:#999;font-style:italic;padding:4px 8px}
.search-btn{left:622px;top:42px;width:25px;height:19px;background:var(--red);display:flex;align-items:center;justify-content:center}
.nav{left:0;top:74px;width:773px;height:36px;background:linear-gradient(#d72a2f,var(--red-dark));display:flex;padding-left:155px}
.nav a{color:var(--white);text-decoration:none;font-family:"PT Sans Narrow",sans-serif;font-size:12px;line-height:36px;padding:0 18px;border-right:1px solid rgba(0,0,0,.2);box-shadow:1px 0 0 rgba(255,255,255,.15)}
.nav a:last-child{border:none;box-shadow:none}
/* hero */
.hero{left:0;top:110px;width:773px;height:291px;background:linear-gradient(#d9d9d9,#eaeaea)}
.finder{left:80px;top:133px;width:157px;height:249px;background:var(--red);border-radius:4px 0 0 4px;padding:10px 6px}
.finder h2{font-weight:400;font-size:15px;color:var(--white);font-variant:small-caps;text-align:center;margin-bottom:12px}
.tabs{display:flex;gap:6px;justify-content:center;margin-bottom:10px}
.tabs span{background:#3a3a3a;border:1px solid #fff;color:#fff;font-size:8px;padding:5px 7px;border-radius:2px}
.select{height:20px;background:#fff;border-radius:2px;margin-bottom:9px;position:relative}
.select:after{content:"";position:absolute;right:8px;top:7px;width:4px;height:4px;border-right:1px solid #555;border-bottom:1px solid #555;transform:rotate(45deg)}
.row{display:flex;align-items:center;gap:6px}
.miles{width:66px;height:20px;background:#fff;border-radius:2px;font-size:7px;font-style:italic;color:#555;padding:6px 8px}
.of{color:#fff;font-size:8px}
.zip{width:52px;height:20px;background:#fff;border-radius:2px}
.go{margin:12px 2px 0 auto;width:63px;height:18px;background:#222;border:1px solid #fff;border-radius:10px;color:#fff;font-size:10px;font-style:italic;text-align:center;line-height:16px}
.finder p{color:#fff;font-size:7px;text-align:right;margin-top:5px;line-height:11px}
.hero-photo{left:237px;top:133px;width:462px;height:249px;background:linear-gradient(#8a9a80 0%,#6b6f6b 40%,#1e2126 60%,#4a4d50 100%);border-radius:0 4px 4px 0}
.caption{left:237px;top:345px;width:462px;height:37px;background:rgba(40,40,40,.75);color:#fff;font-size:13px;font-variant:small-caps;padding:10px 32px;border-radius:0 0 4px 0}
.dots{right:18px;top:15px;display:flex;gap:2px}
.dots i{width:7px;height:7px;border:1px solid #fff;display:block}
.dots i:first-child{background:#f0c020}
/* listings */
.card{top:425px;width:168px;height:195px;background:#fff;border:1px solid #e6e6e6;box-shadow:0 6px 6px -4px rgba(0,0,0,.15)}
.card .pic{position:absolute;left:4px;top:4px;width:158px;height:88px;background:linear-gradient(160deg,#9aa4ad,#cfd4d8 60%,#7b848a)}
.price{position:absolute;left:0;top:4px;width:70px;height:40px;background:var(--red);clip-path:polygon(0 0,100% 0,0 100%);color:#fff;font-weight:700;font-size:12px}
.price span{position:absolute;left:2px;top:10px;transform:rotate(-25deg)}
.avatar{position:absolute;left:6px;top:101px;width:50px;height:50px;border-radius:50%;background:linear-gradient(#8a5a3c,#c9a283)}
.info{position:absolute;left:57px;top:97px;font-size:8.5px;color:#777;line-height:15.5px}
.info .ind{padding-left:38px}
.more{position:absolute;right:21px;top:166px;width:53px;height:18px;background:#1a1a1a;color:#fff;font-size:8.5px;text-align:center;line-height:18px;border-radius:6px}
.divider{left:20px;top:660px;width:733px;height:10px;background:radial-gradient(ellipse at top,rgba(0,0,0,.12),transparent 70%)}
/* welcome */
.welcome h2{font-weight:400;font-size:16px;color:#444}
.welcome h2 b,.sec h2 b{color:var(--red);font-weight:400}
.welcome h3{font-size:10px;font-weight:700;color:#444;margin:10px 0 8px}
.welcome p{font-size:7.5px;line-height:11.6px;color:#333;text-align:justify;margin-bottom:11px}
.red-more{color:var(--red);font-size:8px}
.video{left:464px;top:701px;width:223px;height:128px;background:#111;padding:3px}
.video .frame{width:100%;height:108px;background:linear-gradient(160deg,#c9cbc6,#777 45%,#222 75%)}
.play{position:absolute;left:99px;top:48px;width:26px;height:17px;background:#111;border-radius:3px}
.play:after{content:"";position:absolute;left:10px;top:4px;border-left:8px solid #fff;border-top:4.5px solid transparent;border-bottom:4.5px solid transparent}
.bar{position:absolute;left:3px;bottom:12px;width:217px;height:2px;background:#555}
.bar i{display:block;width:50px;height:2px;background:var(--red)}
/* lower band */
.band{left:0;top:860px;width:773px;height:238px;background:var(--light);border-top:1px solid #e3e3e3}
.sec h2{font-weight:400;font-size:15px;color:#444}
.thumb{width:97px;height:73px;border:2px solid #ddd;background:linear-gradient(150deg,#8d7a68,#c7c3bd 50%,#6e6155)}
.item-t{font-size:11px;color:#333}
.item-p{font-size:7.5px;line-height:10.5px;color:#333}
.rthumb{width:122px;height:72px;border:2px solid #ddd;background:linear-gradient(#9bbad8,#e2e7ec 45%,#c9ced3 60%,#5f7154)}
.count{width:22px;height:14px;background:#1a1a1a;color:#fff;font-size:7.5px;text-align:center;line-height:14px;border-radius:2px}
/* footer */
.footer{left:0;top:1098px;width:773px;height:102px;background:linear-gradient(#1a2129,#2b323a)}
.footer h4{color:#fff;font-size:12px}
.email{left:93px;top:1139px;width:167px;height:20px;background:#fff;border-radius:2px;font-size:7px;font-style:italic;color:#999;padding:6px 11px}
.subscribe{left:192px;top:1166px;width:67px;height:20px;background:var(--red);color:#fff;font-size:9px;text-align:center;line-height:20px}
.social{left:558px;top:1110px;display:flex;gap:9px}
.social i{width:17px;height:17px;display:block;border-radius:2px}
.flinks{right:70px;top:1134px;color:#eee;font-size:8px;text-align:right;line-height:13.5px}
</style>
</head>
<body>
<header>
  <div class="abs mascot" role="img" aria-label="Cartoon mechanic mascot holding a wrench"></div>
  <div class="abs brand">Query Tobin</div>
  <div class="abs tagline">Buying a Ride?,&nbsp; Selling a Ride?,&nbsp; Ride a Dive?&nbsp; Query Tobin</div>
  <div class="abs phone">
    <svg width="16" height="13" viewBox="0 0 16 13"><path d="M1 4c0-3 14-3 14 0v1h-4V3H5v2H1z" fill="#222"/><rect x="3" y="6" width="10" height="7" rx="1" fill="#222"/><circle cx="8" cy="9.5" r="1.8" fill="#eee"/></svg>
    0400 123 987
  </div>
  <div class="abs search">Search</div>
  <div class="abs search-btn"><svg width="12" height="12" viewBox="0 0 12 12"><circle cx="5" cy="5" r="3.5" fill="none" stroke="#fff" stroke-width="1.8"/><path d="M7.5 7.5L11 11" stroke="#fff" stroke-width="2"/></svg></div>
  <nav class="abs nav">
    <a>Buy</a><a>Sell</a><a>News</a><a>Care Tips</a><a>Finance</a><a>Insurance</a><a>FAQ</a><a>Contact Us</a>
  </nav>
</header>

<section>
  <div class="abs hero"></div>
  <div class="abs finder">
    <h2>Find Used Cars</h2>
    <div class="tabs"><span>Used</span><span>Certified Pre-Owned</span></div>
    <div class="select"></div>
    <div class="select"></div>
    <div class="select"></div>
    <div class="row"><div class="miles">All Miles</div><span class="of">Of</span><div class="zip"></div></div>
    <div class="go">SEARCH</div>
    <p>Search or Customize a Used Car<br>Advanced Search</p>
  </div>
  <div class="abs hero-photo" role="img" aria-label="Black sedan parked in a driveway"></div>
  <div class="abs caption">Viewing and Posting Used Cars for Sale
    <div class="abs dots"><i></i><i></i><i></i></div>
  </div>
</section>

<section>
  <div class="abs card" style="left:84px">
    <div class="pic" role="img" aria-label="Silver compact SUV"></div>
    <div class="price"><span>$123.50</span></div>
    <div class="avatar" role="img" aria-label="Seller profile photo"></div>
    <div class="info">Owners Name : Lena<br>Location : Loreum<br><span class="ind">Ipsum Dollar</span><br><span class="ind" style="padding-left:37px">Newyork</span></div>
    <div class="more">More</div>
  </div>
  <div class="abs card" style="left:297px">
    <div class="pic" role="img" aria-label="Silver sedan"></div>
    <div class="price"><span>$150.70</span></div>
    <div class="avatar" role="img" aria-label="Seller profile photo"></div>
    <div class="info">Owners Name : Lena<br>Location : Loreum<br><span class="ind">Ipsum Dollar</span><br><span class="ind" style="padding-left:37px">Newyork</span></div>
    <div class="more">More</div>
  </div>
  <div class="abs card" style="left:517px">
    <div class="pic" role="img" aria-label="Dark luxury sedan" style="background:linear-gradient(160deg,#8a9077,#2a2c30 55%,#555)"></div>
    <div class="price"><span>$107.50</span></div>
    <div class="avatar" role="img" aria-label="Seller profile photo"></div>
    <div class="info">Owners Name : Owen<br>Location : Loreum<br><span class="ind">Ipsum Dollar</span><br><span class="ind" style="padding-left:37px">Newyork</span></div>
    <div class="more">More</div>
  </div>
  <div class="abs divider"></div>
</section>

<section class="abs welcome" style="left:98px;top:681px;width:328px">
  <h2>Welcome to <b>QueryTobin</b></h2>
  <h3>Mauris Vitae Felis Vestibulum Volutpat.</h3>
  <p>Sed ut perspiciatis unde omnis iste natus error sit voluptatem accusantium doloremque laudantium, totam rem aperiam, eaque ipsa quae ab illo inventore veritatis et quasi architecto beatae vitae dicta sunt explicabo.Sed ut perspiciatis unde omnis iste natus error sit voluptatem accusantium doloremque laudantium, totam rem aperiam,</p>
  <p>Eaque ipsa quae ab illo inventore veritatis et quasi architecto beatae vitae dicta sunt explicabo.Sed ut perspiciatis unde omnis iste natus error sit voluptatem accusantium doloremque laudantium, totam rem aperiam, eaque ipsa quae ab illo inventore veritatis et quasi architecto beatae vitae dicta sunt explicabo.</p>
  <div class="red-more" style="text-align:right;margin-top:-6px">More &gt;&gt;</div>
</section>
<div class="abs video">
  <div class="frame" role="img" aria-label="Video still of a black hatchback"></div>
  <div class="play"></div>
  <div class="bar"><i></i></div>
</div>

<section>
  <div class="abs band"></div>
  <div class="abs sec" style="left:98px;top:874px"><h2>Select Your <b>Car</b></h2></div>
  <div class="abs thumb" style="left:95px;top:903px" role="img" aria-label="Silver sedan in a yard"></div>
  <div class="abs" style="left:198px;top:902px;width:200px">
    <div class="item-t">Uenim Ad Minim Veniam Quis</div>
    <p class="item-p" style="margin:8px 0 4px">Uenim ad minim veniam, quis nostrud laboris nisi utaliquip ex irurdolor into Uenim ad minim veniam, quis nostrud laboris nisi utaliquip ex irurdolor into laboris nisi</p>
    <div class="red-more">More &gt;&gt;</div>
  </div>
  <div class="abs thumb" style="left:95px;top:994px;background:linear-gradient(150deg,#2a2a2a,#a8a49d 50%,#3a342f)" role="img" aria-label="Car interior with leather seats"></div>
  <div class="abs" style="left:198px;top:993px;width:200px">
    <div class="item-t">Uenim Ad Minim Veniam Quis</div>
    <p class="item-p" style="margin:8px 0 4px">Uenim ad minim veniam, quis nostrud laboris nisi utaliquip ex irurdolor into Uenim ad minim veniam, quis nostrud laboris nisi utaliquip ex irurdolor into laboris nisi</p>
    <div class="red-more">More &gt;&gt;</div>
  </div>

  <div class="abs sec" style="left:420px;top:874px"><h2>Featured <b>Reviews</b></h2></div>
  <div class="abs rthumb" style="left:421px;top:905px" role="img" aria-label="Silver compact sedan"></div>
  <div class="abs count" style="left:518px;top:898px">30</div>
  <div class="abs" style="left:551px;top:909px;width:155px">
    <p class="item-p" style="line-height:11.6px">Uenim ad minim veniam, quis nostrud laboris nisi utaliquip ex irurdolor into Uenim ad minim veniam, quis nostrud laboris nisi utaliquip ex irurdolor into laboris nisi utaliquip ex irurdolor into</p>
    <div class="red-more" style="text-align:right;margin-top:-6px">More &gt;&gt;</div>
  </div>
  <div class="abs rthumb" style="left:421px;top:999px;background:linear-gradient(#5f7a4c,#c9cdd2 55%,#8d9096)" role="img" aria-label="Silver sedan by trees"></div>
  <div class="abs count" style="left:518px;top:992px">39</div>
  <div class="abs" style="left:551px;top:1004px;width:155px">
    <p class="item-p" style="line-height:11.6px">Uenim ad minim veniam, quis nostrud laboris nisi utaliquip ex irurdolor into Uenim ad minim veniam, quis nostrud laboris nisi utaliquip ex irurdolor into laboris nisi utaliquip ex irurdolor into</p>
    <div class="red-more" style="text-align:right;margin-top:4px">More &gt;&gt;</div>
  </div>
</section>

<footer>
  <div class="abs footer"></div>
  <div class="abs" style="left:93px;top:1110px"><h4>Newsletter</h4></div>
  <div class="abs email">Your Email Id</div>
  <div class="abs subscribe">Subscribe</div>
  <div class="abs social">
    <i style="background:#3b5ea8"></i><i style="background:#2aa3dd"></i><i style="background:#6a7077"></i><i style="background:#f08a1c"></i><i style="background:#c4161c"></i><i style="background:#8b96a0"></i>
  </div>
  <div class="abs flinks">Buy - Sell - News - Care Tips - Finance - Insurance - FAQ<br>© 2013 QueryTobin, All Rights Reserved</div>
</footer>
</body>
</html>
```